Trifold B2B flyer for software consulting/software futureproofness check / IT company

We need a flyer for a consulting offer for the company "VORANTEK GmbH".

The service involves the analysis and evaluation of software systems in companies; the target group consists of managing directors and IT managers of medium-sized companies in various industries.

The flyer should be modern, uncluttered, serious, and professional. It must inspire trust. A dark background would be preferable.

For content and layout, see PDF/PPTX "Software-Wandel-Fast-Scan-Konzept.pptx|.pdf".

In the appendix you will find further examples of VORANTEK designs, as well as the logo and other images.

-----------
We need a flyer for a consulting offering for the company “VORANTEK GmbH”.

The offering focuses on the analysis and evaluation of software systems within companies. The target audience is managing directors/CEOs and IT managers of mid-sized companies across various industries.

The flyer should be modern, clean, serious, and professional. It must build trust. A dark background is preferred.

Please refer to the PDF/PPTX “Software-Wandels-Fast-Scan-konzept.pptx|.pdf” for the content and the layout/ordering of the sections.

Attached you will also find additional examples of VORANTEK designs, as well as the logo and further images.

Target Market(s)

Medium businesses, various industries. Target group: CEO, CIO, IT lead

Industry/Entity Type

Medium-Businesses, various Industries.

Font styles to use
Sans Serif
Other font styles liked:
• Myriad

Colors

Designer to choose colors to be used in the design.

Requirements
Must have
• Branding of my company, professional, stylish, clean, trustful design

```html
<!DOCTYPE html>
<html lang="de">
<head>
<meta charset="utf-8">
<title>VORANTEK – Software Zukunfts Quick Check</title>
<link rel="stylesheet" href="https://fonts.googleapis.com/css2?family=Barlow+Condensed:wght@600;700;800&family=Source+Sans+3:wght@400;600;700&display=swap">
<style>
:root{
  --stage:#dcdddf;
  --navy:#0f1e3d;
  --navy-deep:#0a1530;
  --blue:#1f5fc4;
  --blue-bright:#2a78e0;
  --sky:#8fb8ee;
  --paper:#ffffff;
  --ink:#1b2436;
  --muted:#55627a;
}
*{box-sizing:border-box;margin:0;padding:0}
html,body{width:851px;height:1200px;overflow:hidden}
body{background:var(--stage);font-family:"Source Sans 3",sans-serif;color:var(--ink);position:relative}
.sheet{position:absolute;left:58px;width:735px;box-shadow:0 6px 18px rgba(0,0,0,.25);overflow:hidden;background:var(--paper)}
.sheet--outer{top:34px;height:548px;display:flex}
.sheet--inner{top:620px;height:548px}
.head{font-family:"Barlow Condensed",sans-serif;font-weight:700;text-transform:uppercase;color:var(--blue);letter-spacing:.3px}

/* outer sheet panels */
.panel{width:245px;height:100%;position:relative}
.panel--situation{background:var(--paper);padding:24px 18px 18px 20px}
.panel--situation .head{font-size:17px;margin-bottom:7px}
.panel--situation p{font-size:9.4px;line-height:1.45;color:var(--muted);margin-bottom:22px}
.question-list{list-style:none}
.question-list li{display:flex;gap:8px;font-size:9.4px;line-height:1.4;color:var(--ink);margin-bottom:14px}
.question-list svg{flex:0 0 11px;margin-top:2px}

.panel--contact{background:linear-gradient(180deg,var(--blue-bright),var(--blue));color:#fff;text-align:center;padding:28px 20px}
.portrait{width:92px;height:92px;border-radius:50%;margin:0 auto 14px;background:radial-gradient(circle at 50% 40%,#c9d3e2,#6f86aa);border:3px solid #fff}
.contact-name{font-family:"Barlow Condensed",sans-serif;font-weight:700;font-size:22px;letter-spacing:.5px}
.contact-title{font-size:8px;font-weight:700;letter-spacing:1px;margin-bottom:8px}
.contact-bio{font-size:7.8px;line-height:1.4;opacity:.9;margin-bottom:18px}
.contact-label{font-size:10px;font-weight:700;margin-bottom:8px}
.pill{display:flex;align-items:center;gap:8px;background:var(--navy);border-radius:3px;padding:6px 10px;font-size:8.5px;font-weight:600;margin:0 auto 7px;width:170px}
.brand{font-family:"Source Sans 3",sans-serif;font-weight:700;letter-spacing:1.5px;display:flex;align-items:center;gap:7px}
.brand-mark{width:12px;height:12px;background:currentColor;display:inline-block}
.panel--contact .brand{position:absolute;bottom:26px;left:0;right:0;justify-content:center;font-size:17px}

.panel--cover{background:var(--navy);color:#fff;padding:0}
.cover-shape{position:absolute;inset:0}
.cover-title{position:absolute;top:50px;left:18px;right:10px}
.cover-title .line1{font-family:"Barlow Condensed",sans-serif;font-weight:800;font-size:34px;line-height:.95;text-transform:uppercase}
.cover-title .line2{display:inline-block;margin-top:6px;background:var(--blue-bright);font-family:"Barlow Condensed",sans-serif;font-weight:800;font-size:44px;line-height:1;padding:2px 8px;text-transform:uppercase}
.cover-note{position:absolute;top:236px;left:18px;width:170px;background:#fff;color:var(--ink);padding:7px 10px;font-size:9px;line-height:1.3}
.cover-note strong{display:block;font-size:11px}
.cover-claim{position:absolute;top:318px;left:18px;font-family:"Barlow Condensed",sans-serif;font-weight:700;font-size:17px;line-height:1.05;text-transform:uppercase}
.panel--cover .brand{position:absolute;bottom:28px;right:22px;font-size:19px}

/* inner sheet */
.inner-head{background:linear-gradient(180deg,var(--blue-bright),var(--blue));height:128px;text-align:center;color:#fff;padding-top:10px}
.inner-head .line1{font-family:"Barlow Condensed",sans-serif;font-weight:800;font-size:50px;line-height:.95}
.inner-head .line2{font-family:"Barlow Condensed",sans-serif;font-weight:800;font-size:62px;line-height:.95}
.inner-band{background:var(--navy-deep);color:#fff;text-align:center;font-family:"Barlow Condensed",sans-serif;font-weight:700;font-size:17px;padding:7px 0;letter-spacing:.3px}
.inner-intro{font-size:9.6px;line-height:1.45;color:var(--muted);padding:11px 26px 6px;text-align:center}
.columns{display:flex;gap:18px;padding:12px 20px}
.column{flex:1}
.column .head{font-size:14px;border-bottom:2px solid var(--blue);padding-bottom:3px;margin-bottom:9px}
.column ul{list-style:none}
.column li{font-size:9.6px;line-height:1.45;margin-bottom:11px}
.column li b{display:block;font-size:10px}
.price{margin-top:14px;font-size:9.6px;line-height:1.5}
.price b{display:block;font-size:10.5px}
</style>
</head>
<body>

<section class="sheet sheet--outer" aria-label="Außenseite">
  <div class="panel panel--situation">
    <h2 class="head">Ausgangslage</h2>
    <p>Geschäftskritische Systeme sind oft gewachsen. Die Diskussion über „weiter so“, „Ablösung“ oder „Modernisierung“ wird häufig aus dem Bauch heraus geführt. Der Quick Check liefert eine fundierte Grundlage für Entscheidungen, ohne ein großes Projekt starten zu müssen.</p>
    <h2 class="head">Typische Fragen</h2>
    <ul class="question-list">
      <li><svg width="11" height="11" viewBox="0 0 11 11"><rect x=".5" y=".5" width="10" height="10" fill="none" stroke="#1f5fc4"/><path d="M2.5 5.5l2 2 4-4" fill="none" stroke="#1f5fc4" stroke-width="1.4"/></svg>Ist das Bestandssystem langfristig noch tragfähig?</li>
      <li><svg width="11" height="11" viewBox="0 0 11 11"><rect x=".5" y=".5" width="10" height="10" fill="none" stroke="#1f5fc4"/><path d="M2.5 5.5l2 2 4-4" fill="none" stroke="#1f5fc4" stroke-width="1.4"/></svg>Welche Risiken bestehen bei Technologie, Know-how und Sicherheit?</li>
      <li><svg width="11" height="11" viewBox="0 0 11 11"><rect x=".5" y=".5" width="10" height="10" fill="none" stroke="#1f5fc4"/><path d="M2.5 5.5l2 2 4-4" fill="none" stroke="#1f5fc4" stroke-width="1.4"/></svg>Lohnt sich eine Modernisierung oder ist eine Ablösung – und wenn ja, wann – sinnvoll?</li>
      <li><svg width="11" height="11" viewBox="0 0 11 11"><rect x=".5" y=".5" width="10" height="10" fill="none" stroke="#1f5fc4"/><path d="M2.5 5.5l2 2 4-4" fill="none" stroke="#1f5fc4" stroke-width="1.4"/></svg>Welche Investitionen sind in den nächsten Jahren zu erwarten?</li>
      <li><svg width="11" height="11" viewBox="0 0 11 11"><rect x=".5" y=".5" width="10" height="10" fill="none" stroke="#1f5fc4"/><path d="M2.5 5.5l2 2 4-4" fill="none" stroke="#1f5fc4" stroke-width="1.4"/></svg>Wie gut passt das System zu künftigen Anforderungen?</li>
      <li><svg width="11" height="11" viewBox="0 0 11 11"><rect x=".5" y=".5" width="10" height="10" fill="none" stroke="#1f5fc4"/><path d="M2.5 5.5l2 2 4-4" fill="none" stroke="#1f5fc4" stroke-width="1.4"/></svg>Welche nächsten Schritte sind realistisch und priorisiert?</li>
    </ul>
  </div>

  <div class="panel panel--contact">
    <div class="portrait" role="img" aria-label="Porträtfoto des Ansprechpartners"></div>
    <div class="contact-name">JONAS WELTER</div>
    <div class="contact-title">DIPLOM-INFORMATIKER (FH)</div>
    <p class="contact-bio">Mehr als 25 Jahre Erfahrung in Entwicklung, Architektur und Modernisierung von Unternehmenssoftware im Mittelstand.</p>
    <div class="contact-label">Kontakt</div>
    <div class="pill"><svg width="11" height="11" viewBox="0 0 24 24"><path fill="#fff" d="M6.6 10.8a15 15 0 006.6 6.6l2.2-2.2c.3-.3.7-.4 1-.2 1.1.4 2.3.6 3.6.6.6 0 1 .4 1 1V20c0 .6-.4 1-1 1A17 17 0 013 4c0-.6.4-1 1-1h3.5c.6 0 1 .4 1 1 0 1.3.2 2.5.6 3.6.1.3 0 .7-.2 1z"/></svg>0351 / 4870 - 2216 - 0</div>
    <div class="pill"><svg width="11" height="11" viewBox="0 0 24 24"><path fill="#fff" d="M2 5h20v14H2zm2 2v.5l8 5 8-5V7z"/></svg>kontakt@vorantek-beratung.de</div>
    <div class="pill"><svg width="11" height="11" viewBox="0 0 24 24"><circle cx="12" cy="12" r="9" fill="none" stroke="#fff" stroke-width="2"/><path d="M3 12h18M12 3c3 3 3 15 0 18M12 3c-3 3-3 15 0 18" fill="none" stroke="#fff" stroke-width="1.5"/></svg>www.vorantek-beratung.de</div>
    <div class="brand"><span class="brand-mark"></span>VORANTEK</div>
  </div>

  <div class="panel panel--cover">
    <svg class="cover-shape" width="245" height="548" viewBox="0 0 245 548" aria-hidden="true">
      <polygon points="150,0 245,0 245,260" fill="#1f5fc4"/>
      <polygon points="200,0 245,0 245,130" fill="#8fb8ee"/>
      <polygon points="245,330 245,548 120,548" fill="#1a3a78"/>
    </svg>
    <div class="cover-title">
      <div class="line1">Software<br>Zukunfts</div>
      <div class="line2">Quick<br>Check</div>
    </div>
    <div class="cover-note"><strong>Bestandssysteme:</strong>Weiter investieren, Modernisieren oder Ersetzen?</div>
    <div class="cover-claim">Mehr<br>Klarheit<br>in wenigen<br>Tagen</div>
    <div class="brand"><span class="brand-mark"></span>VORANTEK</div>
  </div>
</section>

<section class="sheet sheet--inner" aria-label="Innenseite">
  <header class="inner-head">
    <div class="line1">SOFTWARE ZUKUNFTS</div>
    <div class="line2">QUICK CHECK</div>
  </header>
  <div class="inner-band">BESTANDSSYSTEME: WEITER INVESTIEREN, MODERNISIEREN ODER ERSETZEN?</div>
  <p class="inner-intro">Der Quick Check bietet den schnellen Einstieg in Orientierung und Objektivierung. Er stellt die Basis für eine detaillierte Analyse des Bestandssystems in Punkto Zukunftsfähigkeit und Handlungsoptionen dar.</p>
  <div class="columns">
    <div class="column">
      <h3 class="head">Fragestellungen</h3>
      <ul>
        <li>Wie stabil ist das System technisch und organisatorisch?</li>
        <li>Wo liegen die größten Kostentreiber (Wartung, Änderungen, Betrieb)?</li>
        <li>Wie hoch ist die Abhängigkeit von einzelnen Personen oder Lieferanten?</li>
        <li>Welche Risiken entstehen, wenn nichts passiert?</li>
        <li>Welche Optionen sind realistisch – und zu welchem Aufwand?</li>
      </ul>
      <div class="price"><b>Preis &amp; Dauer</b>Festpreis ab 4.900 € (zzgl. MwSt.)<br>2–3 Wochen, inkl. Abschlusstermin</div>
    </div>
    <div class="column">
      <h3 class="head">Vorgehen</h3>
      <ul>
        <li><b>Kickoff-Workshop (1/2 Tag)</b>Ziele, Rahmen, Ansprechpartner und Zugänge festlegen.</li>
        <li><b>Sichtung &amp; Analyse</b>Code, Architektur, Dokumentation, Betrieb und Schnittstellen.</li>
        <li><b>Interviews (2–4)</b>Gespräche mit Fachbereich, IT und Betrieb zu Nutzung und Problemen.</li>
        <li><b>Bewertung</b>Einordnung nach Technik, Wirtschaftlichkeit und Risiko.</li>
        <li><b>Ergebnispräsentation (1/2 Tag)</b>Vorstellung und Diskussion mit der Geschäftsleitung.</li>
      </ul>
    </div>
    <div class="column">
      <h3 class="head">Ergebnisse / Lieferobjekte</h3>
      <ul>
        <li><b>Bericht kompakt</b>Status, Risiken, Stärken und Schwächen auf 10–15 Seiten.</li>
        <li><b>3 Optionen skizziert</b>Weiterführen, Modernisieren, Ersetzen – mit Aufwand und Zeitrahmen.</li>
        <li><b>Next Steps</b>Konkrete, priorisierte Empfehlungen für die nächsten Monate.</li>
        <li><b>Fazit für die Entscheidung</b>Klare Aussage für Geschäftsführung und IT-Leitung.</li>
      </ul>
    </div>
  </div>
</section>

</body>
</html>
```